Update to Current Website (www.lrcapitalplanning.example)

5 pages is what I need. This is one cohesive design across all pages.

I would like to create an update to the current website with a fresh look and feel that is mobile compatible.

All content will stay the same. The only thing I want removed from the current content is "Returns for every turning chapter" that is on the main page.

The website address is www.lrcapitalplanning.example

need the site to be mobile-optimized/responsive

During the contest, you can submit one design or page, and in the handover, once selected, the winner will provide the rest of the pages.

Updates

This has been upgraded to a coded project. Looking for something clean, professional, and goes with my newly designed logo. Please read brief for details! Added Monday, February 1, 2016

Target Market(s)

Consumers

Industry/Entity Type

Financial Planning

Coding

Coded - Design and coding required

Number of Pages Required

5+ page

Requirements
Must have
• Really like pagelatticer builder Harlow Template or www.silverbirchcounsel.example
• Something eye catching, simple, and easy to navigate

```html
<!DOCTYPE html>
<html lang="en">
<head>
<meta charset="utf-8">
<title>L&amp;R Capital Planning</title>
<link href="https://fonts.googleapis.com/css2?family=Oswald:wght@300;400&family=Roboto:ital,wght@0,300;0,400;0,500;1,400;1,500&display=swap" rel="stylesheet">
<style>
:root{
  --gold:#c8911f;
  --ink:#3a3a3a;
  --muted:#8a8a8a;
  --footer:#222222;
  --footer-line:#3a3a3a;
  --field:#d9d9d9;
  --white:#ffffff;
}
*{box-sizing:border-box;margin:0;padding:0}
html,body{width:914px;height:1200px;overflow:hidden;background:var(--white)}
body{position:relative;font-family:"Roboto",Arial,sans-serif;color:var(--ink)}
.abs{position:absolute}

/* header */
.brand{left:78px;top:14px}
.brand-name{display:flex;align-items:center;gap:6px;font-size:17px;font-weight:500;color:var(--ink);white-space:nowrap}
.brand-dot{width:12px;height:12px;border-radius:50%;background:var(--gold)}
.brand-tag{font-size:6px;color:var(--ink);margin-top:5px;letter-spacing:.2px}
.nav{top:34px;left:341px;font-size:8.8px;font-weight:400;color:#555;white-space:nowrap}
.nav a{color:inherit;text-decoration:none;position:absolute}
.nav .active{color:var(--gold)}

/* hero */
.hero{left:0;top:84px;width:914px;height:345px;background:linear-gradient(100deg,#8a9a4e 0%,#a8ab78 30%,#c9b8a2 55%,#d8c2ae 75%,#b79a82 100%)}
.hero-copy{left:76px;top:130px;font-family:"Oswald",Arial,sans-serif;text-shadow:2px 2px 2px rgba(0,0,0,.55);line-height:1}
.hero-l1{font-size:40px;font-weight:300;color:#e0a22a}
.hero-l2{font-size:22px;font-weight:300;color:var(--white);margin-top:6px}
.hero-l3{font-size:41px;font-weight:400;color:var(--white);margin-top:8px}
.hero-arrows{left:76px;top:373px;display:flex;gap:18px}

/* welcome */
.welcome{left:0;top:458px;width:914px;text-align:center}
.welcome h1{font-size:17px;font-weight:400;color:var(--ink)}
.hl{color:var(--gold)}
.welcome p{font-size:8.6px;line-height:16px;color:var(--ink);margin:14px auto 0;width:700px;font-weight:300}

/* feature cards */
.card{top:572px;width:370px;text-align:center}
.card-photo{width:370px;height:222px;border:1px solid #ddd;padding:2px;background:var(--white)}
.card-photo div{width:100%;height:100%}
.card h2{font-size:15px;font-weight:400;color:#555;margin-top:20px}
.card p{font-size:8.4px;line-height:16px;color:var(--muted);margin-top:8px;padding:0 7px;font-weight:300}
.btn-outline{display:inline-block;margin-top:16px;width:77px;height:30px;line-height:28px;border:1px solid var(--gold);border-radius:3px;color:var(--gold);font-size:9px;font-style:italic;font-weight:500}

/* footer */
.footer{left:0;top:960px;width:914px;height:240px;background:var(--footer);color:var(--white)}
.col h3{font-size:12.8px;font-weight:500;letter-spacing:.2px}
.col ul{list-style:none;font-size:10px;line-height:15.7px;font-weight:300}
.col p{font-size:9.5px;line-height:14px;font-weight:300}
.divider{width:1px;height:127px;background:var(--footer-line);top:43px}
.field{width:186px;height:28px;background:var(--field);font-size:8px;color:#777;padding:9px 8px}
.subscribe{width:78px;height:27px;background:var(--gold);border-radius:3px;font-size:9.5px;font-weight:500;text-align:center;line-height:27px}
.social{display:flex;align-items:center;font-size:9px;font-weight:300;height:21px;margin-bottom:3px}
.social-box{width:21px;height:21px;border:1px solid #777;margin-right:16px}
.badge{left:755px;top:158px;width:84px;height:47px;background:#3a3a3a;border-bottom:8px solid #b8262b}
.baseline{left:76px;top:205px;width:763px;height:1px;background:var(--footer-line)}
.copyright{left:77px;top:212px;font-size:9px;color:#bbb;font-weight:300}
</style>
</head>
<body>

<header>
  <div class="abs brand">
    <div class="brand-name"><span class="brand-dot"></span>L&amp;R Capital Planning</div>
    <div class="brand-tag">Tailored planning for every chapter since 1968</div>
  </div>
  <nav class="abs nav">
    <a class="active" style="left:0">HOME</a>
    <a style="left:65px">ABOUT US</a>
    <a style="left:147px">WEALTH MANAGEMENT SERVICES</a>
    <a style="left:329px">RESOURCES</a>
    <a style="left:419px">ACCOUNT ACCESS</a>
  </nav>
</header>

<section class="abs hero" role="img" aria-label="Photo of a smiling woman relaxing in a striped hammock with a book"></section>
<div class="abs hero-copy">
  <div class="hero-l1">PLANNING</div>
  <div class="hero-l2">FOR YOUR</div>
  <div class="hero-l3">LASTING FUTURE</div>
</div>
<div class="abs hero-arrows">
  <svg width="29" height="29" viewBox="0 0 29 29"><circle cx="14.5" cy="14.5" r="13" fill="none" stroke="#fff" stroke-width="2.5"/><path d="M17 8.5 L11 14.5 L17 20.5" fill="none" stroke="#fff" stroke-width="2.5"/></svg>
  <svg width="29" height="29" viewBox="0 0 29 29"><circle cx="14.5" cy="14.5" r="13" fill="none" stroke="#fff" stroke-width="2.5"/><path d="M12 8.5 L18 14.5 L12 20.5" fill="none" stroke="#fff" stroke-width="2.5"/></svg>
</div>

<section class="abs welcome">
  <h1>WELCOME TO <span class="hl">L&amp;R CAPITAL</span> PLANNING</h1>
  <p>There are many variations of passages of Lorem Ipsum available, but the majority have suffered alteration in some form, by injected humour, or randomised words which don't look even slightly believable. If you are going to use a passage of Lorem Ipsum, you need to be sure there isn't anything embarrassing hidden in the middle of text.<br>All the Lorem Ipsum generators on the Internet tend to repeat predefined chunks as necessary, making this the first true generator on the Internet..</p>
</section>

<article class="abs card" style="left:75px">
  <div class="card-photo"><div role="img" aria-label="Photo of a team of business people in suits in an office" style="background:linear-gradient(180deg,#d7dde2 0%,#6d7885 45%,#1f2a3a 100%)"></div></div>
  <h2>ABOUT <span class="hl">OUR TEAM</span></h2>
  <p>Praesentium voluptatum deleniti atque corrupti quos dolores et quas molestias excepturi sint occaecati cupiditate non provident, similique sunt in culpa qui officia deserunt mollitia animi, id est laborum et dolorum fuga. Et harum quidem rerum facilis.</p>
  <span class="btn-outline">READ MORE</span>
</article>

<article class="abs card" style="left:470px">
  <div class="card-photo"><div role="img" aria-label="Photo of many raised hands giving thumbs up against a blue sky" style="background:linear-gradient(180deg,#5fc2d8 0%,#a9d9e6 45%,#c99a80 100%)"></div></div>
  <h2>COMPLIMENTARY <span class="hl">INVESTMENT REVIEW</span></h2>
  <p>Praesentium voluptatum deleniti atque corrupti quos dolores et quas molestias excepturi sint occaecati cupiditate non provident, similique sunt in culpa qui officia deserunt mollitia animi, id est laborum et dolorum fuga. Et harum quidem rerum facilis.</p>
  <span class="btn-outline">READ MORE</span>
</article>

<footer class="abs footer">
  <div class="abs col" style="left:76px;top:37px">
    <h3>MARKET SUMMARY</h3>
    <ul style="margin-top:18px">
      <li>Hotme</li><li>About</li><li>Services</li><li>Mathengine</li><li>Solutions</li><li>Contact</li>
    </ul>
  </div>
  <div class="abs divider" style="left:227px"></div>

  <div class="abs col" style="left:261px;top:35px;width:136px">
    <h3>INDUSTRY NEWS</h3>
    <p style="margin-top:17px">Pleasure and praising pain was born and complete account.</p>
    <p style="margin-top:15px">Pleasure and praising pain was born and complete account.</p>
  </div>
  <div class="abs divider" style="left:423px"></div>

  <div class="abs col" style="left:456px;top:35px">
    <h3>MEDIA &amp; NEWSLETTERS</h3>
    <p style="font-size:8px;color:#bbb;margin-top:4px">normal distribution of letters dfhfjgk</p>
    <div class="field" style="margin-top:9px">email</div>
    <div class="field" style="margin-top:6px">Password</div>
    <div class="subscribe" style="margin:7px 0 0 109px">SUBSCRIDE</div>
  </div>
  <div class="abs divider" style="left:673px"></div>

  <div class="abs col" style="left:710px;top:37px">
    <h3>SOCIAL MEDIA LINKS</h3>
  </div>
  <div class="abs" style="left:705px;top:75px">
    <div class="social"><span class="social-box"></span>Chatterly</div>
    <div class="social"><span class="social-box"></span>Peeplet</div>
    <div class="social"><span class="social-box"></span>Circlespace</div>
  </div>
  <div class="abs badge" role="img" aria-label="Industry award badge"></div>

  <div class="abs baseline"></div>
  <div class="abs copyright">Copyright © lrcapitalplanning.example - all rights reserved</div>
</footer>

</body>
</html>
```